Business card design for online Mandarin Learning School

We need a business card design for our online language learning school called "Sunny Kite Academy for Mandarin Learning". Our existing website is https://www.sunnykiteacademy.com
We have our logo already. We would like to see our business card design that can make our online teaching services to be innovative, young, energetic and fun to learn. Prefer to have a certain level of color matching with our website. Apart from "Sunny Kite Academy", need to specifically state "for Mandarin Learning" as well on the business card.

```html
<!DOCTYPE html>
<html lang="en">
<head>
<meta charset="utf-8">
<title>Sunny Kite Academy – Business Cards</title>
<link href="https://fonts.googleapis.com/css2?family=Open+Sans:wght@400;600;700&display=swap" rel="stylesheet">
<style>
  :root {
    --teal: #1aa3b1;
    --coral: #e05858;
    --slate: #7b7b7b;
    --ink: #555555;
    --paper: #f4f4f4;
    --backdrop: #3b3b3b;
  }
  * { box-sizing: border-box; margin: 0; padding: 0; }
  html, body {
    width: 1200px; height: 1021px; overflow: hidden;
    background: var(--backdrop);
    font-family: "Open Sans", Arial, sans-serif;
  }
  .stage {
    width: 1200px; height: 1021px;
    display: flex; flex-direction: column;
    align-items: center; justify-content: center; gap: 60px;
  }
  .card {
    position: relative;
    width: 700px; height: 400px;
    background: var(--paper);
    overflow: hidden;
  }
  .edge-band {
    position: absolute; left: 0; right: 0; bottom: 0; height: 16px;
    display: flex;
  }
  .edge-band span { height: 100%; }
  .edge-band .grey { background: var(--slate); }
  .edge-band .red { background: var(--coral); }
  .edge-band .teal { background: var(--teal); }

  .brand {
    display: flex; align-items: center; gap: 14px;
    color: var(--teal); font-weight: 600; letter-spacing: 1px;
  }
  .brand-dot {
    width: 22px; height: 22px; border-radius: 50%;
    background: var(--coral); flex: none;
  }
  .brand-name { line-height: 1.2; }

  /* front */
  .card--front {
    display: flex; flex-direction: column; align-items: center; justify-content: center;
    padding-bottom: 16px;
  }
  .card--front .brand-name { font-size: 34px; }
  .card--front .brand-name small { display: block; font-size: 22px; }
  .front-url {
    margin-top: 44px; font-size: 18px; color: var(--ink); letter-spacing: 2px;
  }

  /* back */
  .card--back {
    display: flex; align-items: center; padding: 0 40px 16px 44px;
  }
  .card--back .brand { width: 300px; }
  .card--back .brand-name { font-size: 24px; }
  .card--back .brand-name small { display: block; font-size: 16px; }
  .divider {
    width: 1px; height: 150px; background: var(--slate); margin: 0 30px 0 26px;
  }
  .contact-name { font-size: 26px; font-weight: 700; color: var(--teal); }
  .contact-role { font-size: 19px; color: var(--ink); margin-bottom: 22px; }
  .contact-list { list-style: none; }
  .contact-list li {
    display: flex; align-items: center; gap: 8px;
    font-size: 19px; color: var(--ink); line-height: 1.35;
  }
  .contact-list svg { width: 17px; height: 17px; flex: none; }
</style>
</head>
<body>
<main class="stage">

  <section class="card card--front">
    <div class="brand">
      <span class="brand-dot"></span>
      <div class="brand-name">SUNNY KITE ACADEMY<small>FOR MANDARIN LEARNING</small></div>
    </div>
    <p class="front-url">www.sunnykiteacademy.com</p>
    <div class="edge-band">
      <span class="grey" style="width:16%"></span><span class="red" style="width:14%"></span><span class="teal" style="width:14%"></span><span class="grey" style="width:14%"></span><span class="red" style="width:14%"></span><span class="teal" style="width:14%"></span><span class="grey" style="width:14%"></span>
    </div>
  </section>

  <section class="card card--back">
    <div class="brand">
      <span class="brand-dot"></span>
      <div class="brand-name">SUNNY KITE ACADEMY<small>FOR MANDARIN LEARNING</small></div>
    </div>
    <div class="divider"></div>
    <div class="contact">
      <p class="contact-name">Daniel Harwood</p>
      <p class="contact-role">Founder</p>
      <ul class="contact-list">
        <li>
          <svg viewBox="0 0 24 24"><path fill="var(--coral)" d="M6.6 10.8a15.2 15.2 0 0 0 6.6 6.6l2.2-2.2c.3-.3.7-.4 1-.2 1.1.4 2.3.6 3.6.6.6 0 1 .4 1 1V20c0 .6-.4 1-1 1A17 17 0 0 1 3 4c0-.6.4-1 1-1h3.5c.6 0 1 .4 1 1 0 1.3.2 2.5.6 3.6.1.3 0 .7-.2 1z"/></svg>
          (555) 213-4870
        </li>
        <li>
          <svg viewBox="0 0 24 24"><rect x="2" y="5" width="20" height="14" fill="none" stroke="var(--coral)" stroke-width="2"/><path d="M2 5l10 8 10-8" fill="none" stroke="var(--coral)" stroke-width="2"/></svg>
          hello@sunnykiteacademy.com
        </li>
        <li>
          <svg viewBox="0 0 24 24" fill="none" stroke="var(--coral)" stroke-width="2"><circle cx="12" cy="12" r="10"/><path d="M2 12h20M12 2c3 3 3 17 0 20M12 2c-3 3-3 17 0 20"/></svg>
          www.sunnykiteacademy.com
        </li>
      </ul>
    </div>
    <div class="edge-band">
      <span class="grey" style="width:16%"></span><span class="red" style="width:14%"></span><span class="teal" style="width:14%"></span><span class="grey" style="width:14%"></span><span class="red" style="width:14%"></span><span class="teal" style="width:14%"></span><span class="grey" style="width:14%"></span>
    </div>
  </section>

</main>
</body>
</html>
```